New Business Card Needed

I need a new business card for Willowmere Kitchen & Bath.
Logo is attached as well a my photo. Note: Make the logo Navy Blue.
Here is the text:
Desmond Ferrick
GC/Owner
Linden Falls NC
704-555-0183
desmond@willowmereKB.example
www.willowmereKB.example
Tag line on card: CRAFT | COMFORT | ON SCHEDULE | ON COST
Trim size: 2.56" X 2.56"
This is where we aim to cut the cards.
Safe area: 2.4" X 2.4"
Make sure any important aspects of your design such as text and logos are inside of the safe area, otherwise they may be cut off.
Bleed area: 2.71 X 2.71
Make sure that your background extends to fill the bleed to avoid your Business Cards having white edges when trimmed.
On the back side. Use photo of kitchen attached.

```html
<!DOCTYPE html>
<html lang="en">
<head>
<meta charset="utf-8">
<title>Willowmere Kitchen &amp; Bath – Business Cards</title>
<link rel="stylesheet" href="https://fonts.googleapis.com/css2?family=Alegreya+Sans:wght@400;500;700;800&display=swap">
<style>
  :root {
    --page-bg: #6e6e71;
    --card-dark: #262626;
    --kitchen-deep: #2a211b;
    --kitchen-mid: #4a3a2e;
    --kitchen-light: #6b5a4c;
    --white: #ffffff;
    --text-soft: #f1f1f1;
    --emboss: #3a3a3a;
    --portrait-dark: #3b3d42;
    --portrait-mid: #7d6a5e;
  }
  * { box-sizing: border-box; margin: 0; padding: 0; }
  html, body {
    width: 1200px; height: 900px; overflow: hidden;
    background: var(--page-bg);
    font-family: "Alegreya Sans", sans-serif;
  }
  .card {
    position: absolute; top: 266px;
    width: 369px; height: 369px; overflow: hidden;
  }
  .card--front { left: 195px; }
  .card--back { left: 607px; background: var(--card-dark); }

  .brand-name { font-weight: 500; text-transform: uppercase; line-height: 1; }
  .brand-name__main { display: block; font-size: 36px; letter-spacing: .02em; }
  .brand-name__sub { display: block; font-size: 16px; letter-spacing: .24em; margin-top: 8px; }

  /* Front */
  .kitchen-photo {
    position: absolute; inset: 0;
    background:
      radial-gradient(ellipse at 55% 70%, rgba(150,140,130,.35), transparent 55%),
      linear-gradient(180deg, var(--kitchen-deep) 0%, var(--kitchen-mid) 45%, var(--kitchen-light) 70%, var(--kitchen-deep) 100%);
  }
  .card--front .brand-name {
    position: absolute; left: 0; right: 0; top: 158px;
    text-align: center; color: var(--white);
  }
  .tagline {
    position: absolute; left: 0; right: 0; top: 326px;
    text-align: center; color: var(--white);
    font-weight: 800; font-size: 14px; letter-spacing: .02em;
  }

  /* Back */
  .card--back .brand-name {
    position: absolute; left: 48px; top: 66px;
    color: var(--emboss);
  }
  .portrait {
    position: absolute; left: 23px; top: 202px;
    width: 144px; height: 144px;
    border: 5px solid var(--white);
    background: linear-gradient(160deg, var(--portrait-dark) 0%, var(--portrait-mid) 60%, var(--portrait-dark) 100%);
  }
  .contact {
    position: absolute; left: 179px; top: 198px;
    color: var(--text-soft);
  }
  .contact__name { font-weight: 700; font-size: 18px; color: var(--white); line-height: 22px; }
  .contact__title { font-size: 14px; line-height: 22px; margin-bottom: 16px; }
  .contact__line { font-size: 13px; line-height: 23px; white-space: nowrap; }
</style>
</head>
<body>
  <section class="card card--front">
    <div class="kitchen-photo" role="img" aria-label="Photo of a finished kitchen with wood cabinets, white island and bar stools, darkened"></div>
    <p class="brand-name"><span class="brand-name__main">Willowmere</span><span class="brand-name__sub">Kitchen &amp; Bath</span></p>
    <p class="tagline">CRAFT | COMFORT | ON SCHEDULE | ON COST</p>
  </section>

  <section class="card card--back">
    <p class="brand-name"><span class="brand-name__main">Willowmere</span><span class="brand-name__sub">Kitchen &amp; Bath</span></p>
    <div class="portrait" role="img" aria-label="Portrait photo of the owner"></div>
    <div class="contact">
      <p class="contact__name">Desmond Ferrick</p>
      <p class="contact__title">GC/Owner</p>
      <p class="contact__line">Linden Falls NC</p>
      <p class="contact__line">704-555-0183</p>
      <p class="contact__line">desmond@willowmereKB.example</p>
      <p class="contact__line">www.willowmereKB.example</p>
    </div>
  </section>
</body>
</html>
```